Velmira Body Oil Label for 4 -8 oz bottles

We are selling 4 and 8 oz body oils and need a label to put on our bottles. I'm not sure if we want a label for the front and also the back of the bottle or just one label in the front. You can give me examples of each way. Attached is our logo on a blue background but the background will change colors depending on the scent as specified in the design description. Our bottle will be either clear or white with a pump spray type lid as shown in the attached example. Attached are also our design criteria which is needed for the labels.
Updates

We have decided to use the disc top cap and not the pump spray cap. If you are able to, please show us the design on the 4 oz bottle with the disc top cap. Thanks

Target Market(s)

women

Industry/Entity Type

skincare, cosmetics

Font styles to use
Serif
Sans Serif

Requirements
Must have
• stylish name for each scented oil which contrasts the font in the logo. Also must have darker colors since the logo colors are lighter.
Nice to have
• Border around the labels, maybe one solid color or maybe two complimenting colors which go well with the fragrnace name
Should not have
• background colors that match the logo colors

```html
<!DOCTYPE html>
<html lang="en">
<head>
<meta charset="utf-8">
<title>Velmira Body Oil Label – Wildwood</title>
<link href="https://fonts.googleapis.com/css2?family=Cormorant+Garamond:ital,wght@0,400;0,500;0,600;1,400&display=swap" rel="stylesheet">
<style>
  :root {
    --page: #ffffff;
    --sage-top: #b3ccaf;
    --sage-light: #d3dfcf;
    --band-green: #6b9863;
    --band-green-edge: #8bb284;
    --side-green: #80ad73;
    --cream: #efe9d6;
    --cream-light: #f3efe0;
    --logo-green: #86b07e;
    --tagline: #6f8f69;
    --label-light: #f1ecdc;
    --size-text: #7a8a58;
  }
  * { margin: 0; padding: 0; box-sizing: border-box; }
  html, body {
    width: 1200px; height: 1200px; overflow: hidden;
    background: var(--page);
    font-family: "Cormorant Garamond", Georgia, serif;
  }
  .canvas { position: relative; width: 1200px; height: 1200px; }

  .front-label {
    position: absolute; left: 467px; top: 581px;
    width: 273px; height: 464px;
    display: flex; flex-direction: column;
  }
  .front-label__top {
    height: 202px;
    background: linear-gradient(180deg, var(--sage-top) 0%, var(--sage-light) 100%);
    display: flex; flex-direction: column; align-items: center;
  }
  .brand {
    margin-top: 62px;
    display: flex; align-items: center; gap: 8px;
    color: var(--logo-green);
    font-size: 40px; font-weight: 400; line-height: 1;
  }
  .brand__dot {
    width: 9px; height: 9px; border-radius: 50%;
    background: var(--logo-green);
  }
  .taglines {
    margin-top: 34px;
    text-align: center;
    color: var(--tagline);
    font-size: 14.5px; line-height: 16.5px;
  }
  .front-label__band {
    height: 98px;
    background: linear-gradient(90deg, var(--band-green-edge) 0%, var(--band-green) 45%, var(--band-green) 70%, #7aa071 100%);
    color: var(--label-light);
    text-align: center;
    padding-top: 8px;
  }
  .scent-name {
    font-size: 40px; font-weight: 400; line-height: 44px; letter-spacing: 1px;
  }
  .scent-type {
    font-size: 22px; font-style: italic; line-height: 26px;
  }
  .front-label__bottom {
    flex: 1;
    background: linear-gradient(180deg, var(--cream-light) 0%, var(--cream) 100%);
    display: flex; flex-direction: column; align-items: center;
  }
  .bouquet {
    margin-top: 10px;
    width: 114px; height: 118px;
    border-radius: 50% 50% 40% 40%;
    background: radial-gradient(circle at 40% 35%, #ef7a5a 0%, #e9c64a 35%, #4f7fb8 60%, #2f5e52 85%);
    opacity: 0.85;
  }
  .volume {
    margin-top: 11px;
    color: var(--size-text);
    font-size: 12px; font-weight: 600; letter-spacing: 0.3px;
  }

  .side-label {
    position: absolute; top: 783px; height: 98px;
    background: var(--side-green);
    border-radius: 3px;
    color: var(--label-light);
    font-size: 7.6px; font-style: italic; line-height: 12px;
    text-align: center;
    display: flex; flex-direction: column; justify-content: center;
    padding: 0 20px;
  }
  .side-label--ingredients { left: 286px; width: 178px; }
  .side-label--directions { left: 743px; width: 173px; height: 96px; }
</style>
</head>
<body>
<div class="canvas">

  <div class="side-label side-label--ingredients">
    <p>Ingredients:</p>
    <p>Cocos Nucifera (Coconut) Oil, Prunus Amygdalus Dulcis (Almond) Oil, Vitis Vinifera (Grapeseed) Oil, Sesamum Indicum (Sesame) Seed Oil, Simmondsia Chinensis (Jojoba) Oil, Tocopheryl Acetate (Vitamin E). Essential oils, and fragrances.</p>
  </div>

  <div class="front-label">
    <div class="front-label__top">
      <div class="brand"><span class="brand__dot"></span><span>Velmira</span></div>
      <div class="taglines">
        <p>Non-Greasy</p>
        <p>With Vitamin E</p>
        <p>Ultra Moisturizing</p>
      </div>
    </div>
    <div class="front-label__band">
      <p class="scent-name">Wildwood</p>
      <p class="scent-type">Jojoba Body Oil</p>
    </div>
    <div class="front-label__bottom">
      <div class="bouquet" role="img" aria-label="Colourful folk-style flower bouquet illustration"></div>
      <p class="volume">50 ml ℮ 8 fl. oz.</p>
    </div>
  </div>

  <div class="side-label side-label--directions">
    <p>Directions:</p>
    <p>Apply a small amount to skin and massage until absorbed. Use daily for best results.</p>
    <p>Warnings / Disclaimers:</p>
    <p>For external use only. Avoid contact with eyes. Discontinue use if irritation occurs.</p>
  </div>

</div>
</body>
</html>
```